Refresh of The Marston Collective business card

Update business card design using existing primary logo. Names, numbers, etc. are too hard to read on current design.

Target Market(s)

We are a CPA firm.

Industry/Entity Type

Accountant

Contact Information for Business Card

update current card

Colors
0355a3
3176b5
85acd3
0792cd

Requirements
Must have
• Easier to read phone numbers and names
• Use existing logo
Nice to have
• We love our color scheme and current TMC logo. But the names and phone numbers are too small and card just look old and stale.

```html
<!DOCTYPE html>
<html lang="en">
<head>
<meta charset="utf-8">
<title>The Marston Collective – Business Card Options</title>
<link href="https://fonts.googleapis.com/css2?family=Fira+Sans:wght@400;500;600&display=swap" rel="stylesheet">
<style>
  :root {
    --brand-blue: #0355a3;
    --brand-mid: #3176b5;
    --brand-light: #85acd3;
    --brand-cyan: #0792cd;
    --navy: #063a72;
    --ink: #0a2f5e;
    --grey-text: #4a4f57;
    --card-edge: #9a9a9a;
    --page: #ffffff;
  }
  * { box-sizing: border-box; margin: 0; padding: 0; }
  html, body { width: 1200px; height: 1200px; overflow: hidden; background: var(--page); }
  body { position: relative; font-family: "Fira Sans", sans-serif; }

  .card { position: absolute; width: 450px; height: 270px; overflow: hidden; }
  .card--back {
    background: radial-gradient(ellipse 70% 80% at 52% 48%, #1363bd 0%, #0a4a98 45%, #052a5a 100%);
  }
  .card--front { background: #fff; border: 1px solid var(--card-edge); }

  .row-one .card { top: 292px; }
  .row-two .card { top: 645px; }
  .card--back { left: 150px; }
  .card--front { left: 600px; }

  /* logo lockup */
  .lockup { position: absolute; display: flex; align-items: center; gap: 12px; }
  .lockup__disc { border-radius: 50%; flex: none; }
  .lockup__name {
    font-weight: 600; font-size: 26px; line-height: 1.02; letter-spacing: 0.5px;
  }
  .lockup__tag {
    display: block; margin-top: 6px; font-weight: 600; font-size: 6px;
    letter-spacing: 2px; text-transform: uppercase;
  }
  .card--back .lockup { left: 112px; top: 78px; }
  .card--back .lockup__disc { width: 76px; height: 76px; border: 3px solid #fff; }
  .card--back .lockup__name, .card--back .lockup__tag { color: #fff; }

  .card--front .lockup { left: 102px; top: 40px; }
  .card--front .lockup__disc {
    width: 82px; height: 82px; border: 3px solid #444;
    background: radial-gradient(circle at 40% 35%, var(--brand-mid), var(--navy));
  }
  .card--front .lockup__name { color: var(--brand-blue); }
  .card--front .lockup__tag { color: var(--grey-text); }

  .website {
    position: absolute; left: 0; width: 460px; top: 226px; text-align: center;
    color: #fff; font-size: 19px; letter-spacing: 0.6px;
  }

  /* contact area */
  .contact-band { position: absolute; left: 0; right: 0; top: 158px; bottom: 0; }
  .card--banded .contact-band { background: var(--navy); }
  .person { position: absolute; left: 34px; top: 21px; font-size: 19px; font-weight: 400; letter-spacing: 0.3px; }
  .address { position: absolute; left: 34px; top: 56px; font-size: 12.5px; line-height: 18.5px; letter-spacing: 0.3px; }
  .details { position: absolute; right: 22px; top: 19px; list-style: none; }
  .details li {
    display: flex; justify-content: flex-end; align-items: center; gap: 9px;
    font-size: 12.5px; height: 18.3px; letter-spacing: 0.3px;
  }
  .details svg { width: 13px; height: 13px; flex: none; }

  .card--banded .person, .card--banded .address, .card--banded .details li { color: #fff; }
  .card--banded .icon-disc { fill: var(--brand-mid); }
  .card--banded .icon-glyph { fill: var(--navy); }

  .card--plain .person { color: var(--ink); font-size: 19.5px; }
  .card--plain .address, .card--plain .details li { color: var(--grey-text); }
  .card--plain .icon-disc { fill: var(--ink); }
  .card--plain .icon-glyph { fill: #fff; }
</style>
</head>
<body>
<svg width="0" height="0" style="position:absolute" aria-hidden="true">
  <symbol id="icon-phone" viewBox="0 0 20 20">
    <circle class="icon-disc" cx="10" cy="10" r="10"/>
    <path class="icon-glyph" d="M6.2 4.8l2 2.1-1.1 1.5c.8 1.7 2 2.9 3.6 3.7l1.5-1.1 2.1 2-1.4 2c-4.3-.6-7.9-4.2-8.5-8.5z"/>
  </symbol>
  <symbol id="icon-fax" viewBox="0 0 20 20">
    <circle class="icon-disc" cx="10" cy="10" r="10"/>
    <path class="icon-glyph" d="M6.5 4.5h7v3h-7zM5 8.5h10v5H5zM7 12h6v3.5H7z"/>
  </symbol>
  <symbol id="icon-mobile" viewBox="0 0 20 20">
    <circle class="icon-disc" cx="10" cy="10" r="10"/>
    <path class="icon-glyph" d="M7 4h6v12H7zM8.2 5.5v8h3.6v-8z"/>
  </symbol>
  <symbol id="icon-mail" viewBox="0 0 20 20">
    <circle class="icon-disc" cx="10" cy="10" r="10"/>
    <path class="icon-glyph" d="M5 6.5h10v7H5zM5.6 7l4.4 3.4L14.4 7z"/>
  </symbol>
</svg>

<section class="row-one">
  <div class="card card--back">
    <div class="lockup">
      <span class="lockup__disc"></span>
      <div><div class="lockup__name">The Marston<br>Collective</div><span class="lockup__tag">Certified Public Accountants</span></div>
    </div>
    <p class="website">www.marstoncollective.com</p>
  </div>
  <div class="card card--front card--banded">
    <div class="lockup">
      <span class="lockup__disc"></span>
      <div><div class="lockup__name">The Marston<br>Collective</div><span class="lockup__tag">Certified Public Accountants</span></div>
    </div>
    <div class="contact-band">
      <p class="person">Nolan R. Whitby, CPA</p>
      <p class="address">318 Linden Grove Rd. Suite 104<br>Oakfield, Florida 32099</p>
      <ul class="details">
        <li>555.214.7830 <svg><use href="#icon-phone"/></svg></li>
        <li>555.214.7831 <svg><use href="#icon-fax"/></svg></li>
        <li>555.386.9042 <svg><use href="#icon-mobile"/></svg></li>
        <li>nolan@marstoncollective.com <svg><use href="#icon-mail"/></svg></li>
      </ul>
    </div>
  </div>
</section>

<section class="row-two">
  <div class="card card--back">
    <div class="lockup">
      <span class="lockup__disc"></span>
      <div><div class="lockup__name">The Marston<br>Collective</div><span class="lockup__tag">Certified Public Accountants</span></div>
    </div>
    <p class="website">www.marstoncollective.com</p>
  </div>
  <div class="card card--front card--plain">
    <div class="lockup">
      <span class="lockup__disc"></span>
      <div><div class="lockup__name">The Marston<br>Collective</div><span class="lockup__tag">Certified Public Accountants</span></div>
    </div>
    <div class="contact-band">
      <p class="person">Nolan R. Whitby, CPA</p>
      <p class="address">318 Linden Grove Rd. Suite 104<br>Oakfield, Florida 32099</p>
      <ul class="details">
        <li>555.214.7830 <svg><use href="#icon-phone"/></svg></li>
        <li>555.214.7831 <svg><use href="#icon-fax"/></svg></li>
        <li>555.386.9042 <svg><use href="#icon-mobile"/></svg></li>
        <li>nolan@marstoncollective.com <svg><use href="#icon-mail"/></svg></li>
      </ul>
    </div>
  </div>
</section>
</body>
</html>
```